Quill Pet Shop Homepage

We are a pet shop, we focus on dog food / cat food / rodents & bird food

Based on WooCommerce

It should be a simple but professional homepage with an informative start page. In the shop it should then be possible to shop for products/manufacturers etc. Navigation/Filter menu on the left would be ideal.

Next menus:
ABOUT US
CONTACT
DOG
CAT
HOLDER

My Account - Login
My Cart

Footer:
Conditions
payment options
social media

In addition to our logo, I have attached 2 example pages from another shop which we would use as a guideline.

Target Market(s)

pet store

Industry/Entity Type

Animal, Pet Shop

Coding

Coded - Design and coding required

Number of Pages Required

1 page

Font styles to use
Sans Serif

Colors
0054AA
0677BA
7BADD7
CADEEF
E8F1F8

Requirements
Must have
• Main Page, Contact, About Us, Shop, Check Out, Member Login, Mailchimp Marketing - We work with WooCommerce

```html
<!DOCTYPE html>
<html lang="en">
<head>
<meta charset="utf-8">
<title>Quill Pet Shop</title>
<link rel="stylesheet" href="https://fonts.googleapis.com/css2?family=Montserrat:wght@600;700;800&family=Roboto:wght@400;500&display=swap">
<style>
:root{
  --blue:#0677BA;
  --blue-deep:#0054AA;
  --blue-mid:#0a6cc0;
  --blue-bright:#1e88e5;
  --blue-soft:#7BADD7;
  --blue-pale:#CADEEF;
  --blue-ice:#E8F1F8;
  --ink:#111;
  --text:#333;
  --muted:#666;
  --grey-bg:#f5f5f5;
  --card:#f0f0f0;
  --footer:#000;
  --star:#f5a623;
  --white:#fff;
}
*{box-sizing:border-box;margin:0;padding:0}
html,body{width:1200px;height:3490px;overflow:hidden;background:var(--white)}
body{position:relative;font-family:"Roboto",Arial,sans-serif;color:var(--text)}
.abs{position:absolute}
h1,h2,h3,.mont{font-family:"Montserrat",Arial,sans-serif}

.promo-bar{top:0;left:0;width:1200px;height:33px;background:var(--blue);color:var(--white);font-size:15px;text-align:center;line-height:33px}
.site-header{top:33px;left:0;width:1200px;height:73px;background:var(--white)}
.brand{position:absolute;left:112px;top:14px;width:160px}
.brand-name{display:flex;align-items:center;gap:8px;font-family:"Montserrat",sans-serif;font-weight:700;font-size:17px;color:var(--blue-deep)}
.brand-dot{width:28px;height:28px;border-radius:50%;background:var(--blue-deep)}
.brand-tag{font-size:9px;letter-spacing:2px;color:var(--muted);margin:3px 0 0 52px}
.main-nav a{position:absolute;top:24px;font-size:15px;color:var(--ink);text-decoration:none}
.main-nav a.active{color:var(--blue)}
.account-link{position:absolute;left:762px;top:22px;font-family:"Montserrat",sans-serif;font-weight:700;font-size:15px;color:var(--blue-deep)}
.auth-group{position:absolute;left:899px;top:14px;height:37px;display:flex;border:2px solid var(--blue-deep)}
.auth-group span{display:flex;align-items:center;gap:7px;font-family:"Montserrat",sans-serif;font-weight:700;font-size:15px;padding:0 12px}
.btn-login{background:var(--blue-deep);color:var(--white);width:99px}
.btn-cart{color:var(--blue-deep);width:101px}

.hero{top:106px;left:0;width:1200px;height:598px;background:var(--blue-mid);overflow:hidden}
.hero-circle{position:absolute;left:610px;top:34px;width:840px;height:840px;border-radius:50%;background:var(--white)}
.hero-packs{position:absolute;left:530px;top:158px;width:370px;height:460px;border-radius:14px;background:linear-gradient(135deg,#2a9e8e,#8fb0a0 60%,#9fb8a8)}
.hero-dog{position:absolute;left:876px;top:190px;width:324px;height:410px;border-radius:120px 40px 0 0;background:linear-gradient(160deg,#b06a36,#7a4524 55%,#d9cfc6)}
.hero-copy{position:absolute;left:112px;top:152px;color:var(--white)}
.hero-copy .kicker{font-family:"Montserrat",sans-serif;font-weight:700;font-size:18px}
.hero-copy h1{font-weight:800;font-size:50px;margin-top:12px;letter-spacing:.5px}
.hero-copy p{font-size:14px;line-height:23px;margin-top:10px;width:400px}
.btn-primary{display:inline-block;background:var(--blue-bright);color:var(--white);font-family:"Montserrat",sans-serif;font-weight:700;font-size:16px;width:147px;height:46px;line-height:46px;text-align:center;margin-top:26px}

.section-title{font-family:"Montserrat",sans-serif;font-weight:800;font-size:35px;color:var(--ink);text-align:center;width:1200px;left:0}
.product{position:absolute;top:888px;width:236px}
.product .thumb{height:252px;background:var(--card);display:flex;align-items:center;justify-content:center}
.product .thumb div{width:160px;height:140px;border-radius:8px}
.product h3{font-weight:700;font-size:19px;color:var(--ink);margin:20px 0 0 7px}
.product .price{font-size:14px;color:var(--muted);margin:13px 0 0 5px}
.product .shop{display:block;font-family:"Montserrat",sans-serif;font-weight:700;font-size:14px;color:var(--blue-deep);text-decoration:underline;margin:14px 0 0 8px}
.carousel-next{left:1126px;top:1018px}

.about{top:1355px;left:0;width:1200px;height:658px;background:var(--grey-bg)}
.about-art{position:absolute;left:55px;top:75px;width:500px;height:500px;border-radius:50%;background:radial-gradient(circle at 50% 45%,#5aa0e0,#1f6fc8 60%,#1258b0)}
.about h2{position:absolute;left:592px;top:148px;font-weight:800;font-size:35px;color:var(--ink)}
.about p{position:absolute;left:598px;top:207px;width:475px;font-size:15px;line-height:25.8px;color:var(--text)}
.btn-pill{position:absolute;left:594px;top:412px;width:147px;height:45px;border-radius:23px;background:var(--blue-deep);color:var(--white);font-family:"Montserrat",sans-serif;font-weight:700;font-size:14px;line-height:45px;text-align:center}

.testimonials{top:2013px;left:0;width:1200px;height:530px;background:linear-gradient(180deg,#0a66bc,#1064b3 50%,#0d5aa8);color:var(--white);text-align:center}
.testimonials h2{position:absolute;top:68px;width:1200px;font-weight:800;font-size:35px}
.avatars{position:absolute;top:134px;left:528px;width:144px;height:62px}
.avatars span{position:absolute;border-radius:50%;background:linear-gradient(160deg,#d9b49a,#7a5a48);border:2px solid var(--white)}
.testimonials .quote{position:absolute;top:222px;left:220px;width:760px;font-size:15.5px;line-height:26px}
.stars{position:absolute;top:325px;width:1200px;color:var(--star);font-size:15px;letter-spacing:3px}
.t-name{position:absolute;top:344px;width:1200px;font-family:"Montserrat",sans-serif;font-weight:700;font-size:19px}
.t-role{position:absolute;top:378px;width:1200px;font-size:14px}
.dots{position:absolute;top:446px;left:572px;display:flex;gap:4px}
.dots i{width:9px;height:9px;border-radius:50%;background:var(--white)}
.dots i.on{background:transparent;border:2px solid var(--white)}

.how-card{position:absolute;top:2757px;left:450px;width:296px;height:226px;background:var(--white);border-radius:4px;box-shadow:0 2px 14px rgba(0,0,0,.12)}
.feature{position:absolute;top:2707px;width:320px;text-align:center}
.feature .icon{width:84px;height:84px;border-radius:50%;background:var(--blue-deep);margin:0 auto;display:flex;align-items:center;justify-content:center}
.feature h3{font-weight:700;font-size:19px;color:var(--ink);margin-top:26px}
.feature p{font-size:15px;line-height:24px;color:var(--text);margin-top:12px}
.feature a{display:block;font-family:"Montserrat",sans-serif;font-weight:600;font-size:14px;color:var(--blue-deep);text-decoration:none;margin-top:10px}

.site-footer{top:3082px;left:0;width:1200px;height:408px;background:var(--footer);color:var(--white)}
.f-brand{position:absolute;left:119px;top:60px}
.f-brand .name{display:flex;align-items:center;gap:12px;font-family:"Montserrat",sans-serif;font-weight:700;font-size:27px;color:var(--blue-bright)}
.f-brand .name i{width:44px;height:44px;border-radius:50%;background:var(--blue-bright)}
.f-brand .tag{font-size:16px;letter-spacing:2.5px;margin:14px 0 0 88px}
.social{position:absolute;top:210px;left:178px;display:flex;gap:7px}
.social span{width:32px;height:32px;border-radius:50%;background:var(--white);display:flex;align-items:center;justify-content:center}
.social span i{width:8px;height:8px;border-radius:50%;background:var(--blue-deep)}
.f-col{position:absolute;top:60px}
.f-col h4{font-family:"Montserrat",sans-serif;font-weight:700;font-size:19px}
.f-col ul{list-style:none;margin-top:20px}
.f-col li{font-size:15px;height:30px}
.f-col p{font-size:15px;line-height:26px;margin-top:18px;width:290px}
.subscribe{position:absolute;left:803px;top:169px;width:274px;height:41px;border-radius:21px;background:var(--white);color:#999;font-size:15px;line-height:41px;padding-left:20px}
.subscribe b{position:absolute;right:0;top:0;width:44px;height:41px;border-radius:50%;background:var(--blue-deep);display:flex;align-items:center;justify-content:center}
.payments{position:absolute;left:800px;top:252px;display:flex;gap:5px}
.payments i{width:43px;height:27px;border-radius:3px;background:var(--blue-pale)}
.payments i:nth-child(2){background:#f0b800}
.payments i:nth-child(3){background:var(--white)}
.payments i:nth-child(5){background:var(--blue)}
.payments i:nth-child(6){background:#e0452a}
.f-rule{position:absolute;left:112px;top:319px;width:977px;height:1px;background:#333}
.copyright{position:absolute;top:354px;width:1200px;text-align:center;font-size:15px}
.copyright span{color:var(--blue-bright);text-decoration:underline}
</style>
</head>
<body>

<div class="abs promo-bar">Buy One, Get One 50% off.</div>

<header class="abs site-header">
  <div class="brand">
    <div class="brand-name"><span class="brand-dot"></span>QUILL PET</div>
    <div class="brand-tag">PREMIUM PET FOOD</div>
  </div>
  <nav class="main-nav">
    <a class="active" style="left:467px">Home</a>
    <a style="left:546px">Shop</a>
    <a style="left:620px">Support</a>
  </nav>
  <div class="account-link">MY ACCOUNT</div>
  <div class="auth-group">
    <span class="btn-login"><svg width="14" height="15" viewBox="0 0 14 15"><circle cx="7" cy="4" r="3.6" fill="#fff"/><path d="M0 15c0-4 3-6 7-6s7 2 7 6z" fill="#fff"/></svg>LOGIN</span>
    <span class="btn-cart"><svg width="16" height="14" viewBox="0 0 16 14"><path d="M1 5h14l-2 8H3z" fill="none" stroke="#0054AA" stroke-width="2"/><path d="M5 5l3-4 3 4" fill="none" stroke="#0054AA" stroke-width="2"/></svg>CART</span>
  </div>
</header>

<section class="abs hero">
  <div class="hero-circle"></div>
  <div class="hero-packs" role="img" aria-label="Cat food and dog food pouches"></div>
  <div class="hero-dog" role="img" aria-label="Boxer dog looking over a food bowl"></div>
  <div class="hero-copy">
    <div class="kicker">WELCOME TO</div>
    <h1>QUILL PET SHOP</h1>
    <p>Lorem ipsum dolor sit amet, consectetur adipiscing elit, sed do eiusmod tempor incididunt ut labore et dolore magna aliqua.</p>
    <span class="btn-primary">SHOP NOW</span>
  </div>
</section>

<h2 class="abs section-title" style="top:797px">OUR PRODUCTS</h2>

<article class="product" style="left:104px">
  <div class="thumb"><div role="img" aria-label="Dog food pouches" style="background:linear-gradient(135deg,#dfe6ee,#9aa8b8)"></div></div>
  <h3>DOG FOOD</h3><div class="price">$ 156.00</div><a class="shop">SHOP NOW</a>
</article>
<article class="product" style="left:353px">
  <div class="thumb"><div role="img" aria-label="Cat food pouch" style="width:110px;height:170px;background:linear-gradient(160deg,#f5d020,#e8a020)"></div></div>
  <h3>CAT FOOD</h3><div class="price">$ 156.00</div><a class="shop">SHOP NOW</a>
</article>
<article class="product" style="left:602px">
  <div class="thumb"><div role="img" aria-label="Rodent food box" style="width:170px;height:150px;background:linear-gradient(135deg,#3cc8d0,#1f9fb0)"></div></div>
  <h3>RODENTS FOOD</h3><div class="price">$ 156.00</div><a class="shop">SHOP NOW</a>
</article>
<article class="product" style="left:851px">
  <div class="thumb"><div role="img" aria-label="Bird food bag" style="height:100px;background:linear-gradient(90deg,#e8b060,#c85a2a 50%,#e8b060)"></div></div>
  <h3>BIRD FOOD</h3><div class="price">$ 156.00</div><a class="shop">SHOP NOW</a>
</article>
<svg class="abs carousel-next" width="8" height="12" viewBox="0 0 8 12"><path d="M1 1l5 5-5 5" fill="none" stroke="#111" stroke-width="1.6"/></svg>

<section class="abs about">
  <div class="about-art" role="img" aria-label="Circular artwork of dog, cat, rabbit and bird silhouettes over pet food"></div>
  <h2>ABOUT US</h2>
  <p>Lorem ipsum dolor sit amet, consectetur adipiscing elit, sed do eiusmod tempor incididunt ut labore et dolore magna aliqua. Quis ipsum suspendisse ultrices gravida. Risus commodo viverra maecenas accumsan lacus vel facilisis. Lorem ipsum dolor sit amet, consectetur adipiscing elit, sed do eiusmod tempor incididunt ut labore et dolore magna aliqua. Quis ipsum suspendisse ultrices gravida. Risus commodo viverra maecenas accumsan lacus vel facilisis.</p>
  <span class="btn-pill">LEARN MORE</span>
</section>

<section class="abs testimonials">
  <h2>OUR CLIENTS TESTIMONIALS</h2>
  <div class="avatars" role="img" aria-label="Customer portraits">
    <span style="left:4px;top:12px;width:40px;height:40px"></span>
    <span style="left:98px;top:12px;width:40px;height:40px"></span>
    <span style="left:40px;top:0;width:62px;height:62px;border-width:3px"></span>
  </div>
  <p class="quote">Lorem ipsum dolor sit amet, consectetur adipiscing elit, sed do eiusmod tempor incididunt ut labore et dolore magna aliqua. Quis ipsum suspendisse ultrices gravida. Risus commodo viverra maecenas accumsan lacus vel facilisis.</p>
  <div class="stars">★★★★★</div>
  <div class="t-name">Marin T.</div>
  <div class="t-role">Verified Buyer</div>
  <div class="dots"><i></i><i></i><i class="on"></i><i></i><i></i></div>
</section>

<h2 class="abs section-title" style="top:2628px">HOW IT WORK</h2>
<div class="how-card"></div>
<div class="feature" style="left:112px">
  <div class="icon"><svg width="40" height="44" viewBox="0 0 40 44"><circle cx="20" cy="17" r="13" fill="none" stroke="#fff" stroke-width="2"/><path d="M14 17l4 4 8-8" fill="none" stroke="#fff" stroke-width="2"/><path d="M12 28l-4 14 6-3 4 4 2-10M28 28l4 14-6-3-4 4-2-10" fill="none" stroke="#fff" stroke-width="1.6"/></svg></div>
  <h3>Quality</h3>
  <p>Lorem ipsum dolor sit amet,<br>consectetur adipiscing elit, sed do<br>eiusmod tempor incididunt</p>
  <a>Learn More &nbsp;»</a>
</div>
<div class="feature" style="left:438px">
  <div class="icon"><svg width="56" height="56" viewBox="0 0 56 56"><circle cx="28" cy="28" r="25" fill="none" stroke="#fff" stroke-width="2"/><text x="28" y="22" text-anchor="middle" font-family="Roboto,sans-serif" font-size="9" fill="#fff">100%</text><text x="28" y="33" text-anchor="middle" font-family="Roboto,sans-serif" font-size="10" fill="#fff">Natural</text><text x="28" y="42" text-anchor="middle" font-family="Roboto,sans-serif" font-size="6" fill="#fff">PRODUCTS</text></svg></div>
  <h3>100% Natural</h3>
  <p>Lorem ipsum dolor sit amet,<br>consectetur adipiscing elit, sed do<br>eiusmod tempor incididunt</p>
  <a>Learn More &nbsp;»</a>
</div>
<div class="feature" style="left:774px">
  <div class="icon"><svg width="44" height="40" viewBox="0 0 44 40"><circle cx="22" cy="14" r="8" fill="none" stroke="#fff" stroke-width="2"/><path d="M8 38c0-9 6-14 14-14s14 5 14 14" fill="none" stroke="#fff" stroke-width="2"/><path d="M10 14a12 12 0 0 1 24 0" fill="none" stroke="#fff" stroke-width="2"/><rect x="6" y="12" width="5" height="8" fill="#fff"/><rect x="33" y="12" width="5" height="8" fill="#fff"/></svg></div>
  <h3>Exceptional Customer Service</h3>
  <p>Lorem ipsum dolor sit amet,<br>consectetur adipiscing elit, sed do<br>eiusmod tempor incididunt</p>
  <a>Learn More &nbsp;»</a>
</div>

<footer class="abs site-footer">
  <div class="f-brand">
    <div class="name"><i></i>QUILL PET</div>
    <div class="tag">PREMIUM PET FOOD</div>
  </div>
  <div class="social"><span><i></i></span><span><i></i></span><span><i></i></span><span><i></i></span></div>
  <div class="f-col" style="left:439px">
    <h4>Quick Link</h4>
    <ul><li>Privacy Policy</li><li>Return Policy</li><li>Payment Policy</li><li>Terms &amp; Conditions</li><li>Shipping Policy</li></ul>
  </div>
  <div class="f-col" style="left:630px">
    <h4>Support</h4>
    <ul><li>Contact</li><li>FAQ</li><li>Customer Service</li><li>Order Tracking</li></ul>
  </div>
  <div class="f-col" style="left:802px">
    <h4>Subscribe To Our Newsletter</h4>
    <p>Lorem ipsum dolor sit amet, consectetur adipiscing elit, sed do</p>
  </div>
  <div class="subscribe">Enter Your Email<b><svg width="18" height="18" viewBox="0 0 18 18"><path d="M1 8l16-7-6 16-3-6z" fill="#fff"/></svg></b></div>
  <div class="payments" aria-label="Accepted payment methods"><i></i><i></i><i></i><i></i><i></i><i></i></div>
  <div class="f-rule"></div>
  <div class="copyright">©Copyrights 2023 &nbsp;<span>Quill Pet Shop</span> &nbsp; | &nbsp; All Rights Reserved</div>
</footer>

</body>
</html>
```